Quillfen Holdings Business Card Design Project

We have recently rebranded and would like to design new business cards that incorporate the corporate logo - double sided cards with corporate logo on one side and contact details on the other

Target Market(s)

Sophisticated and high net worth investors and finance industry professionals

Industry/Entity Type

Funds Management

Contact Information for Business Card

The card should prominently feature the company name and logo. Other details will be standard contact details for each staff member - name, address, phone, email, website

Colors
0054AA
0677BA
7BADD7
CADEEF
E8F1F8

Requirements
Must have
• Double-sided design with one side prominently featuring the corporate logo and the other side with all standard contact details

```html
<!DOCTYPE html>
<html lang="en">
<head>
<meta charset="utf-8">
<title>Quillfen Holdings — Business Card</title>
<link rel="stylesheet" href="https://fonts.googleapis.com/css2?family=Montserrat:wght@400;500;600;700&display=swap">
<style>
  :root {
    --navy: #1f4676;
    --navy-deep: #1b3f6c;
    --navy-light: #2a5689;
    --ink: #2b2b2b;
    --muted: #4a4a4a;
    --paper: #ffffff;
    --paper-shade: #f3f3f3;
    --backdrop: #d9dbde;
  }
  * { box-sizing: border-box; margin: 0; padding: 0; }
  html, body { width: 1200px; height: 1200px; overflow: hidden; }
  body {
    background: var(--backdrop);
    font-family: "Montserrat", Arial, sans-serif;
    position: relative;
  }
  .card {
    position: absolute;
    left: 220px;
    width: 760px;
    height: 434px;
    border-radius: 30px;
    overflow: hidden;
    box-shadow: 0 10px 28px rgba(0,0,0,0.22);
  }
  .card-front {
    top: 150px;
    background: linear-gradient(180deg, var(--paper) 0%, var(--paper-shade) 100%);
  }
  .card-back {
    top: 630px;
    background: linear-gradient(135deg, var(--navy-light) 0%, var(--navy) 50%, var(--navy-deep) 100%);
    display: flex;
    align-items: center;
    justify-content: center;
  }
  .front-wordmark {
    position: absolute;
    top: 92px;
    right: 70px;
    color: var(--navy);
    font-weight: 600;
    font-size: 30px;
    letter-spacing: 2px;
    text-transform: uppercase;
  }
  .identity {
    position: absolute;
    left: 64px;
    top: 168px;
    padding-left: 18px;
    border-left: 6px solid var(--navy);
  }
  .identity-name {
    color: var(--navy);
    font-weight: 700;
    font-size: 34px;
    line-height: 1;
    letter-spacing: 0.5px;
  }
  .identity-role {
    color: var(--muted);
    font-weight: 400;
    font-size: 15px;
    letter-spacing: 1px;
    margin-top: 6px;
  }
  .contact-list {
    position: absolute;
    left: 88px;
    top: 262px;
    list-style: none;
  }
  .contact-item {
    display: flex;
    align-items: flex-start;
    gap: 12px;
    color: var(--ink);
    font-size: 15px;
    line-height: 1.25;
    margin-bottom: 8px;
  }
  .contact-icon {
    width: 18px;
    height: 18px;
    flex: 0 0 18px;
    margin-top: 1px;
    fill: var(--navy);
  }
  .accent-band {
    position: absolute;
    bottom: 0;
    left: 385px;
    width: 255px;
    height: 14px;
    background: var(--navy);
  }
  .back-wordmark {
    color: var(--paper);
    font-weight: 600;
    font-size: 50px;
    letter-spacing: 4px;
    text-transform: uppercase;
  }
</style>
</head>
<body>
  <section class="card card-front" aria-label="Card front with contact details">
    <div class="front-wordmark">Quillfen Holdings</div>

    <div class="identity">
      <div class="identity-name">ELIAS MARLOW</div>
      <div class="identity-role">CEO | FOUNDER</div>
    </div>

    <ul class="contact-list">
      <li class="contact-item">
        <svg class="contact-icon" viewBox="0 0 24 24" aria-hidden="true"><path d="M6.6 10.8a15.2 15.2 0 0 0 6.6 6.6l2.2-2.2a1 1 0 0 1 1-.25 11.4 11.4 0 0 0 3.6.57 1 1 0 0 1 1 1V20a1 1 0 0 1-1 1A17 17 0 0 1 3 4a1 1 0 0 1 1-1h3.5a1 1 0 0 1 1 1c0 1.25.2 2.45.57 3.6a1 1 0 0 1-.25 1z"/></svg>
        <span>+02 9460 3175</span>
      </li>
      <li class="contact-item">
        <svg class="contact-icon" viewBox="0 0 24 24" aria-hidden="true"><path d="M12 2a10 10 0 1 0 0 20 10 10 0 0 0 0-20zm6.9 6h-3a15.6 15.6 0 0 0-1.3-3.6A8 8 0 0 1 18.9 8zM12 4a14 14 0 0 1 1.9 4h-3.8A14 14 0 0 1 12 4zM4.3 14a8 8 0 0 1 0-4h3.4a16.5 16.5 0 0 0 0 4zm.8 2h3a15.6 15.6 0 0 0 1.3 3.6A8 8 0 0 1 5.1 16zm3-8h-3a8 8 0 0 1 4.3-3.6A15.6 15.6 0 0 0 8.1 8zM12 20a14 14 0 0 1-1.9-4h3.8A14 14 0 0 1 12 20zm2.3-6H9.7a14.7 14.7 0 0 1 0-4h4.6a14.7 14.7 0 0 1 0 4zm.3 5.6a15.6 15.6 0 0 0 1.3-3.6h3a8 8 0 0 1-4.3 3.6zm1.7-5.6a16.5 16.5 0 0 0 0-4h3.4a8 8 0 0 1 0 4z"/></svg>
        <span>www.quillfen-holdings.com</span>
      </li>
      <li class="contact-item">
        <svg class="contact-icon" viewBox="0 0 24 24" aria-hidden="true"><path d="M2 5h20v14H2zm2 2v.5l8 5.5 8-5.5V7l-8 5.5z"/></svg>
        <span>enquiries@quillfen-holdings.com</span>
      </li>
      <li class="contact-item">
        <svg class="contact-icon" viewBox="0 0 24 24" aria-hidden="true"><path d="M12 2a7 7 0 0 0-7 7c0 5.2 7 13 7 13s7-7.8 7-13a7 7 0 0 0-7-7zm0 9.5A2.5 2.5 0 1 1 12 6.5a2.5 2.5 0 0 1 0 5z"/></svg>
        <span>Level 14 Wattle House, 52<br>Ferris Street, Sydney NSW 2000</span>
      </li>
    </ul>

    <div class="accent-band"></div>
  </section>

  <section class="card card-back" aria-label="Card back with company name">
    <div class="back-wordmark">Quillfen Holdings</div>
  </section>
</body>
</html>
```